Business Card Design

We are a manufacturing and distribution company with most of our customer base being supermarkets. We have established brand guidelines that are attached.

```html
<!DOCTYPE html>
<html lang="en">
<head>
<meta charset="utf-8">
<title>Veranto Business Card</title>
<link href="https://fonts.googleapis.com/css2?family=Montserrat:wght@500;800&family=Arimo:wght@400&display=swap" rel="stylesheet">
<style>
  :root {
    --bg-top: #d2d2d2;
    --bg-bottom: #a9a9a9;
    --card-white: #ffffff;
    --brand-blue: #0b68ad;
    --brand-red: #e3262d;
    --ink: #111111;
    --text: #222222;
    --faint-blue: #e6f0f9;
    --faint-red: #fbe7e8;
  }
  * { margin: 0; padding: 0; box-sizing: border-box; }
  html, body { width: 1200px; height: 788px; overflow: hidden; }
  body {
    background: linear-gradient(180deg, var(--bg-top), var(--bg-bottom));
    position: relative;
    font-family: "Arimo", Arial, sans-serif;
  }
  .card {
    position: absolute;
    top: 244px;
    width: 520px;
    height: 300px;
    box-shadow: 0 14px 28px rgba(0,0,0,0.28);
    overflow: hidden;
  }
  .card--front { left: 50px; background: var(--card-white); }
  .card--back { left: 630px; background: var(--brand-blue); }

  .front-decoration {
    position: absolute;
    right: 46px;
    top: 40px;
    width: 210px;
    height: 210px;
    background: linear-gradient(135deg, var(--faint-blue) 50%, var(--faint-red) 50%);
  }
  .company-name {
    position: absolute;
    left: 40px;
    top: 34px;
    font-family: "Montserrat", Arial, sans-serif;
    font-weight: 800;
    font-size: 40px;
    letter-spacing: 2px;
    color: var(--ink);
  }
  .accent-bar {
    position: absolute;
    left: 0;
    top: 104px;
    width: 20px;
    height: 44px;
    background: var(--brand-red);
  }
  .person {
    position: absolute;
    left: 40px;
    top: 104px;
  }
  .person-name {
    font-family: "Montserrat", Arial, sans-serif;
    font-weight: 800;
    font-size: 23px;
    letter-spacing: 1px;
    line-height: 1.1;
  }
  .person-name .first { color: var(--brand-red); }
  .person-name .last { color: var(--brand-blue); }
  .person-title { font-size: 14px; color: var(--text); margin-top: 2px; }

  .address {
    position: absolute;
    left: 40px;
    top: 168px;
    font-size: 13.5px;
    line-height: 1.35;
    color: var(--text);
  }
  .contacts {
    position: absolute;
    left: 40px;
    top: 215px;
    list-style: none;
    font-size: 13.5px;
    line-height: 1.4;
    color: var(--text);
  }
  .contacts li { display: flex; align-items: center; gap: 7px; }
  .contacts svg { width: 12px; height: 12px; flex: none; }

  .back-brand {
    position: absolute;
    left: 0; right: 0;
    top: 112px;
    display: flex;
    align-items: center;
    justify-content: center;
    gap: 16px;
  }
  .back-square { width: 26px; height: 26px; background: var(--brand-red); }
  .back-name {
    font-family: "Montserrat", Arial, sans-serif;
    font-weight: 800;
    font-size: 54px;
    letter-spacing: 3px;
    color: #ffffff;
  }
</style>
</head>
<body>
  <section class="card card--front" aria-label="Card front">
    <div class="front-decoration" aria-hidden="true"></div>
    <h1 class="company-name">VERANTO</h1>
    <div class="accent-bar"></div>
    <div class="person">
      <p class="person-name"><span class="first">DANIEL</span> <span class="last">ORTIZ</span></p>
      <p class="person-title">CEO/Founder</p>
    </div>
    <p class="address">2205 Harlow Street<br>Country Name, AB 40312</p>
    <ul class="contacts">
      <li>
        <svg viewBox="0 0 12 12" aria-hidden="true"><circle cx="6" cy="6" r="6" fill="var(--brand-blue)"/><path d="M4 3.2 5.2 4.6 4.6 5.4a4 4 0 0 0 2 2l.8-.6L8.8 8 8.2 9A5.4 5.4 0 0 1 3 3.8Z" fill="#fff"/></svg>
        555-310-4827
      </li>
      <li>
        <svg viewBox="0 0 12 12" aria-hidden="true"><rect x="0.5" y="2" width="11" height="8" fill="var(--brand-blue)"/><path d="M0.5 2 6 6.5 11.5 2" stroke="#fff" fill="none"/></svg>
        info@veranto.com.au
      </li>
      <li>
        <svg viewBox="0 0 12 12" aria-hidden="true"><circle cx="6" cy="6" r="6" fill="var(--brand-blue)"/><path d="M0 6h12M6 0c-3 3-3 9 0 12M6 0c3 3 3 9 0 12" stroke="#fff" stroke-width="0.8" fill="none"/></svg>
        www.veranto.com.au
      </li>
    </ul>
  </section>

  <section class="card card--back" aria-label="Card back">
    <div class="back-brand">
      <span class="back-square" aria-hidden="true"></span>
      <span class="back-name">VERANTO</span>
    </div>
  </section>
</body>
</html>
```